scentharborline.example business card desing

Design a business card for an contemporary e commerce company that sells fragrances and cosmetics. State of the art , high tech and super very fast delivery

Target Market(s)

e commerce customers like Bramble, Tolvex , and retailers wesites

Industry/Entity Type

Business

Contact Information for Business Card

On the Front :

scentharborline.example with some design element

On the back :
Dr. Marek Thornby
President

Phone ( icom) 555.207.6431
Cell (icon) 555.284.9062
Fax(icon) 555.613.4870
email (icon) marek@scentharborline.example

4815 Cedar Lane
Alderbrook, EX 11990

Colors
b768aa
e667a6
abd036

Requirements
Must have
• all the above content info
Nice to have
• Could have and abstract perfume bottle
Should not have
• no faces, facial features,

```html
<!DOCTYPE html>
<html lang="en">
<head>
<meta charset="utf-8">
<title>scentharborline.example Business Card</title>
<link rel="stylesheet" href="https://fonts.googleapis.com/css2?family=Poppins:wght@400;500;600&display=swap">
<style>
  :root {
    --canvas-bg: #ecebe8;
    --brand-pink: #e8438f;
    --brand-pink-deep: #e0307f;
    --band-white: #ffffff;
    --text-white: #ffffff;
    --photo-light: #dfe6f2;
    --photo-red: #d8344e;
    --photo-magenta: #c8287a;
    --photo-blue: #4a6fc0;
    --shadow: rgba(0, 0, 0, 0.18);
  }
  * { box-sizing: border-box; margin: 0; padding: 0; }
  html, body {
    width: 1200px;
    height: 857px;
    overflow: hidden;
    background: var(--canvas-bg);
    font-family: "Poppins", "Century Gothic", sans-serif;
  }
  .sheet {
    position: relative;
    width: 1200px;
    height: 857px;
    display: flex;
    align-items: center;
    justify-content: center;
    gap: 40px;
  }
  .card {
    position: relative;
    width: 500px;
    height: 286px;
    border-radius: 26px;
    overflow: hidden;
    box-shadow: 0 10px 28px var(--shadow);
  }

  /* Front */
  .card-front__photo {
    position: absolute;
    inset: 0;
    background:
      radial-gradient(ellipse 30% 55% at 22% 62%, var(--photo-red), transparent 70%),
      radial-gradient(ellipse 26% 50% at 82% 50%, var(--photo-magenta), transparent 70%),
      radial-gradient(ellipse 22% 40% at 52% 78%, var(--photo-blue), transparent 72%),
      radial-gradient(ellipse 14% 22% at 55% 12%, #c9a640, transparent 75%),
      linear-gradient(180deg, #f4f6fb 0%, var(--photo-light) 100%);
  }
  .card-front__band {
    position: absolute;
    left: 0;
    right: 0;
    top: 168px;
    height: 50px;
    background: rgba(255, 255, 255, 0.72);
    display: flex;
    align-items: center;
    padding-left: 54px;
  }
  .brand-name {
    font-size: 30px;
    font-weight: 500;
    color: var(--brand-pink);
    letter-spacing: -0.2px;
    white-space: nowrap;
  }

  /* Back */
  .card-back {
    background: var(--brand-pink);
  }
  .card-back__pattern {
    position: absolute;
    inset: 0;
    background: linear-gradient(135deg, var(--brand-pink) 0%, var(--brand-pink-deep) 100%);
  }
  .card-back__band {
    position: absolute;
    left: 0;
    width: 372px;
    top: 76px;
    height: 78px;
    background: var(--band-white);
    display: flex;
    flex-direction: column;
    justify-content: center;
    padding-left: 150px;
  }
  .person-name {
    font-size: 15px;
    font-weight: 600;
    color: var(--brand-pink);
    letter-spacing: 0.3px;
    line-height: 1.2;
    white-space: nowrap;
  }
  .person-title {
    font-size: 11px;
    font-weight: 400;
    color: var(--brand-pink);
    line-height: 1.2;
  }
  .contact-list {
    position: absolute;
    left: 150px;
    top: 166px;
    list-style: none;
    color: var(--text-white);
    font-size: 11.5px;
    line-height: 1;
  }
  .contact-list li {
    display: flex;
    align-items: center;
    gap: 6px;
    margin-bottom: 9px;
    white-space: nowrap;
  }
  .contact-row--phones { gap: 14px; }
  .contact-item {
    display: inline-flex;
    align-items: center;
    gap: 5px;
  }
  .contact-icon {
    width: 11px;
    height: 11px;
    flex: none;
  }
</style>
</head>
<body>
<main class="sheet">

  <section class="card card-front" aria-label="Card front">
    <div class="card-front__photo" role="img" aria-label="Photograph of colourful perfume bottles with a gold cap"></div>
    <div class="card-front__band">
      <span class="brand-name">scentharborline.example</span>
    </div>
  </section>

  <section class="card card-back" aria-label="Card back">
    <div class="card-back__pattern" role="img" aria-label="Pink swirling floral pattern"></div>
    <div class="card-back__band">
      <p class="person-name">Dr. MAREK THORNBY</p>
      <p class="person-title">President</p>
    </div>
    <ul class="contact-list">
      <li class="contact-row--phones">
        <span class="contact-item">
          <svg class="contact-icon" viewBox="0 0 12 12" aria-label="Phone"><circle cx="6" cy="6" r="6" fill="#fff"/><path d="M4 3.2l1 1.3-.6.7c.4.9 1 1.5 1.9 1.9l.7-.6 1.3 1-.5 1.1C5.6 8.4 3.6 6.4 3.4 4z" fill="#e8438f"/></svg>
          555.207.6431
        </span>
        <span class="contact-item">
          <svg class="contact-icon" viewBox="0 0 12 12" aria-label="Cell"><circle cx="6" cy="6" r="6" fill="#fff"/><rect x="4.2" y="2.6" width="3.6" height="6.8" rx="0.7" fill="#e8438f"/><rect x="4.8" y="3.4" width="2.4" height="4.4" fill="#fff"/></svg>
          555.284.9062
        </span>
        <span class="contact-item">
          <svg class="contact-icon" viewBox="0 0 12 12" aria-label="Fax"><circle cx="6" cy="6" r="6" fill="#fff"/><rect x="3" y="5" width="6" height="3.6" rx="0.6" fill="#e8438f"/><rect x="4.2" y="3" width="3.6" height="2.4" fill="#e8438f"/></svg>
          555.613.4870
        </span>
      </li>
      <li>
        <svg class="contact-icon" viewBox="0 0 12 12" aria-label="Email"><circle cx="6" cy="6" r="6" fill="#fff"/><rect x="3" y="4" width="6" height="4.2" fill="#e8438f"/><path d="M3 4l3 2.4L9 4" fill="none" stroke="#fff" stroke-width="0.7"/></svg>
        marek@scentharborline.example
      </li>
      <li>
        <svg class="contact-icon" viewBox="0 0 12 12" aria-label="Address"><circle cx="6" cy="6" r="6" fill="#fff"/><path d="M6 2.6a2.2 2.2 0 0 1 2.2 2.2C8.2 6.4 6 9.2 6 9.2S3.8 6.4 3.8 4.8A2.2 2.2 0 0 1 6 2.6z" fill="#e8438f"/><circle cx="6" cy="4.8" r="0.8" fill="#fff"/></svg>
        4815 Cedar Lane, Alderbrook, EX 11990.
      </li>
    </ul>
  </section>

</main>
</body>
</html>
```